Enhance Landing Page

Actual: https://thebrisalounge.com/aposte-no-horizonte-lp-port/

I need a better design for this page:
Using this shortcodes : https://sturdy.qtvlayouts.net
Rules:
. Keep the page header
. Keep the footer

```html
<!DOCTYPE html>
<html lang="en">
<head>
<meta charset="utf-8">
<title>Coral Haven – Invest in Florida</title>
<link href="https://fonts.googleapis.com/css2?family=Lato:ital,wght@0,300;0,400;0,700;0,900;1,400&display=swap" rel="stylesheet">
<style>
  :root {
    --ink: #222;
    --muted: #666;
    --accent: #5cc28f;
    --red: #e0224f;
    --page: #f4f4f4;
    --white: #fff;
  }
  * { margin: 0; padding: 0; box-sizing: border-box; }
  html, body { width: 1120px; height: 1200px; overflow: hidden; }
  body { font-family: 'Lato', sans-serif; background: var(--page); color: var(--ink); position: relative; }

  .hero {
    position: absolute; left: 0; top: 0; width: 1120px; height: 627px;
    background: linear-gradient(180deg, #5d85b5 0%, #8fb0cf 38%, #6aa6a8 52%, #b9b3a6 62%, #d6cec3 100%);
  }
  .hero__contacts { position: absolute; right: 26px; top: 10px; text-align: right; }
  .hero__phone { display: flex; align-items: center; justify-content: flex-end; gap: 10px;
    font-size: 18px; font-weight: 300; color: #333; letter-spacing: 1.2px; height: 34px; }
  .hero__flag { width: 16px; height: 12px; display: inline-block; }
  .hero__flag--us { background: linear-gradient(180deg, #c8102e 0 15%, #fff 15% 30%, #c8102e 30% 45%, #fff 45% 60%, #c8102e 60% 75%, #fff 75% 90%, #c8102e 90%); }
  .hero__flag--br { background: #229e45; border-radius: 2px; }
  .hero__title {
    position: absolute; left: 0; width: 100%; top: 370px; text-align: center;
    font-size: 40px; font-weight: 300; color: var(--white); line-height: 39px; letter-spacing: 0.5px;
  }
  .hero__title em { font-style: normal; color: var(--red); }
  .hero__button {
    position: absolute; left: 514px; top: 567px; width: 136px; height: 27px; border-radius: 14px;
    background: #0b0b0b; color: var(--white); font-size: 11.5px; font-weight: 700; letter-spacing: 0.8px;
    display: flex; align-items: center; justify-content: center; gap: 10px;
  }

  .nav { position: absolute; left: 0; top: 627px; width: 1120px; height: 78px; background: var(--white); }
  .nav__brand { position: absolute; left: 82px; top: 25px; display: flex; align-items: center; gap: 8px;
    font-size: 22px; font-weight: 900; color: var(--red); letter-spacing: 1px; }
  .nav__brand i { width: 12px; height: 12px; border-radius: 50%; background: var(--red); display: inline-block; }
  .nav__menu { position: absolute; top: 32px; left: 414px; display: flex; align-items: center;
    font-size: 11.8px; color: var(--ink); }
  .nav__item { padding: 0 17px; border-left: 1px solid #e2e2e2; line-height: 10px; }
  .nav__item:first-child { padding-left: 0; border-left: 0; }
  .nav__item--active { color: var(--accent); }
  .nav__search { position: absolute; left: 1012px; top: 35px; }

  .about__photo {
    position: absolute; left: 155px; top: 727px; width: 377px; height: 400px;
    background: linear-gradient(180deg, #73a9d6 0%, #a8c9e2 45%, #c9cccc 62%, #7aa08a 72%, #3cb1ad 80%, #2fa4a3 100%);
  }
  .about__trim { position: absolute; left: 138px; top: 760px; }

  .accordion { position: absolute; left: 571px; top: 765px; width: 460px; }
  .accordion__row { display: flex; align-items: center; gap: 15px; font-size: 14.4px; font-weight: 300;
    letter-spacing: 1px; color: #333; height: 22px; margin-bottom: 7px; }
  .accordion__row--open { color: var(--accent); margin-bottom: 5px; }
  .accordion__radio { width: 12px; height: 12px; border-radius: 50%; border: 1px solid #999; flex: none; position: relative; }
  .accordion__row--open .accordion__radio { border-color: var(--accent); }
  .accordion__row--open .accordion__radio::after { content: ""; position: absolute; left: 2px; top: 2px;
    width: 6px; height: 6px; border-radius: 50%; background: var(--accent); }
  .accordion__body { padding-left: 28px; width: 456px; font-size: 10.5px; line-height: 16.8px; color: var(--muted);
    letter-spacing: 0.95px; margin-bottom: 13px; }
  .accordion__body p { margin-bottom: 16px; }
  .accordion__body p:last-child { margin-bottom: 0; }
  .accordion__body a { color: var(--accent); text-decoration: none; }
  .accordion__quote { font-style: italic; font-weight: 400; font-size: 12px; line-height: 16.8px; color: #555; letter-spacing: 0.8px; }

  .section-kicker { position: absolute; left: 0; width: 1120px; top: 1173px; text-align: center;
    font-size: 12.5px; font-weight: 400; color: var(--accent); letter-spacing: 1px; }
</style>
</head>
<body>
  <header class="hero" role="img" aria-label="Beach photo: palm tree leaning over white sand, a rowing boat and a wooden pier on turquoise water">
    <div class="hero__contacts">
      <div class="hero__phone">+1 (555) 010-4827 <span class="hero__flag hero__flag--us"></span></div>
      <div class="hero__phone">+55 21 5550-2716 <span class="hero__flag hero__flag--br"></span></div>
    </div>
    <h1 class="hero__title">INVEST IN <em>FLORIDA</em> AND EFFECTIVELY<br>TRANQUILITY</h1>
    <div class="hero__button">LEARN MORE
      <svg width="8" height="6" viewBox="0 0 8 6"><path d="M1 1.5 4 4.5 7 1.5" fill="none" stroke="#fff" stroke-width="1.2"/></svg>
    </div>
  </header>

  <nav class="nav">
    <div class="nav__brand"><i></i>CORAL HAVEN</div>
    <div class="nav__menu">
      <span class="nav__item">Home</span>
      <span class="nav__item nav__item--active">About</span>
      <span class="nav__item">Features</span>
      <span class="nav__item">Opportunities</span>
      <span class="nav__item">Newsletter</span>
      <span class="nav__item">Talk to Agent</span>
      <span class="nav__item">Contact Now</span>
    </div>
    <svg class="nav__search" width="13" height="13" viewBox="0 0 13 13"><circle cx="7.5" cy="5.5" r="4.3" fill="none" stroke="#333" stroke-width="1.1"/><path d="M4.5 8.5 1 12" stroke="#333" stroke-width="1.2"/></svg>
  </nav>

  <svg class="about__trim" width="20" height="335" viewBox="0 0 20 335">
    <path d="M18 2 Q5 10 5 40 L5 332" fill="none" stroke="#e6e6e6" stroke-width="2"/>
    <rect x="0" y="88" width="4" height="26" fill="#e4e4e4"/>
    <rect x="0" y="142" width="4" height="46" fill="#e4e4e4"/>
    <rect x="0" y="198" width="4" height="46" fill="#e4e4e4"/>
  </svg>
  <div class="about__photo" role="img" aria-label="Photo of a city skyline with high-rise towers across a turquoise bay under a blue sky"></div>

  <section class="accordion">
    <div class="accordion__row"><span class="accordion__radio"></span>What We Believe.</div>
    <div class="accordion__row accordion__row--open"><span class="accordion__radio"></span>How We Work.</div>
    <div class="accordion__body">
      <p>Carles vegan Goddart cronut plaid Forkline gluten-free distillery. Pug normcore 90's cliche slow-carb direct trade. Deep v uPhone skateboard, tote bag bitters <a>Thunderkits mumblecore</a>. Echo Park ethical listicle, mumblecore umami lo-fi chia lomo tattooed synth.</p>
      <p class="accordion__quote">Health goth flannel hella Goddart, whatever Grey Kettle aesthetic. Coastline Apparel salvia biodiesel cornhole, kogi farm-to-table messenger bag four dollar toast. Forkline Bushwick ennui gentrify.</p>
      <p>Heliotype Wes Andover retro, keffiyeh jean shorts salvia trust fund street art bitters shabby chic Thunderkits. Synth you probably haven't heard of them leggings, sriracha locavore <a>tattooed crucifirights</a>.</p>
    </div>
    <div class="accordion__row"><span class="accordion__radio"></span>Our Passion Is Our Work.</div>
    <div class="accordion__row"><span class="accordion__radio"></span>Some Other Uber Cool Title.</div>
  </section>

  <h2 class="section-kicker">What makes us Different</h2>
</body>
</html>
```